Business Card for staff member of football club SC Brenval

I would like to get a business card template for all staff member of our soccer club.

The card should use as much as possible the 2 colors of the club : Red which is the main color and blue which is the alternative color. It can be balanced between the two like our logo.

I prefer simple and lean design.

Contact Information for Business Card

Bussiness card should have all main stuff as describe here below in must have.

Font styles to use
Sans Serif

Requirements
Must have
• Name : Laurent DESPRATIN
Fonction : Président
Mobile : +41 xx xxx xx xx
Email : first.lastname@scbrenval.ch
Adresse of the club : SC Brenval, 1873 Brenval
Website of the club : www.scbrenval.ch
Nice to have
• Version with and without picture of the staff member

A version for men, a version for women staff member.

```html
<!DOCTYPE html>
<html lang="fr">
<head>
<meta charset="utf-8">
<title>SC Brenval – Carte de visite</title>
<link rel="stylesheet" href="https://fonts.googleapis.com/css2?family=Comfortaa:wght@700&family=Roboto:wght@500;700;900&display=swap">
<style>
  :root {
    --club-red: #e5283a;
    --club-blue: #1f8fd0;
    --ink: #1d1d1f;
    --paper: #ffffff;
    --backdrop: #d9d9d9;
    --photo-tone: #6f6a66;
    --photo-tone-light: #b9b0a8;
  }
  * { margin: 0; padding: 0; box-sizing: border-box; }
  html, body {
    width: 1200px; height: 675px; overflow: hidden;
    background: var(--backdrop);
    font-family: "Roboto", Arial, sans-serif;
  }
  .canvas {
    position: relative; width: 1200px; height: 675px;
    display: flex; align-items: center; justify-content: center; gap: 60px;
  }
  .card {
    position: relative; width: 500px; height: 324px;
    background: var(--paper); border-radius: 12px; overflow: hidden;
    box-shadow: 0 10px 28px rgba(0,0,0,.18);
  }
  .card-bands { position: absolute; inset: 0; width: 100%; height: 100%; }

  .club-mark {
    display: flex; align-items: center; gap: 8px;
    font-family: "Roboto", sans-serif; font-weight: 900;
    color: var(--ink); text-transform: uppercase; letter-spacing: .5px;
    white-space: nowrap;
  }
  .club-mark__dot { border-radius: 50%; background: var(--club-red); flex: none; }

  /* front */
  .card--front .club-mark { position: absolute; left: 30px; top: 40px; font-size: 20px; }
  .card--front .club-mark__dot { width: 22px; height: 22px; }
  .person { position: absolute; right: 28px; top: 52px; text-align: right; }
  .person__name {
    font-family: "Comfortaa", sans-serif; font-weight: 700;
    color: var(--club-red); font-size: 19px; text-transform: uppercase; letter-spacing: .3px;
    white-space: nowrap;
  }
  .person__role {
    font-family: "Comfortaa", sans-serif; font-weight: 700;
    color: var(--club-blue); font-size: 12px; text-transform: uppercase; margin-top: 2px;
  }
  .portrait { position: absolute; left: 146px; top: 84px; width: 150px; height: 180px; }
  .contact-list {
    position: absolute; left: 306px; top: 140px; list-style: none;
    font-size: 10.5px; font-weight: 700; color: var(--ink);
  }
  .contact-list li { display: flex; align-items: center; gap: 7px; height: 19px; white-space: nowrap; }
  .contact-list svg { width: 10px; height: 10px; flex: none; fill: var(--club-blue); }

  /* back */
  .card--back .club-mark {
    position: absolute; left: 50%; top: 44%; transform: translate(-50%, -50%); font-size: 32px;
  }
  .card--back .club-mark__dot { width: 34px; height: 34px; }
</style>
</head>
<body>
<main class="canvas">

  <section class="card card--front" aria-label="Recto de la carte">
    <svg class="card-bands" viewBox="0 0 500 324" aria-hidden="true">
      <polygon points="0,262 202,262 222,284 0,284" fill="var(--club-red)"/>
      <polygon points="242,272 500,272 500,300 268,300" fill="var(--club-blue)"/>
    </svg>

    <div class="club-mark"><span class="club-mark__dot"></span>SC Brenval</div>

    <header class="person">
      <h1 class="person__name">Laurent Despratin</h1>
      <p class="person__role">Président</p>
    </header>

    <svg class="portrait" viewBox="0 0 150 180">
      <polyline points="6,160 6,6 110,6" fill="none" stroke="var(--club-red)" stroke-width="5"/>
      <polyline points="144,20 144,150 108,176 40,176" fill="none" stroke="var(--club-blue)" stroke-width="5"/>
      <defs>
        <linearGradient id="portrait-fill" x1="0" y1="0" x2="0" y2="1">
          <stop offset="0" stop-color="var(--photo-tone-light)"/>
          <stop offset="1" stop-color="var(--photo-tone)"/>
        </linearGradient>
      </defs>
      <path d="M16,16 H134 V144 L104,166 H16 Z" fill="url(#portrait-fill)" role="img" aria-label="Photo du membre du staff"/>
    </svg>

    <ul class="contact-list">
      <li><svg viewBox="0 0 10 10"><path d="M5 0a3.5 3.5 0 0 0-3.5 3.5C1.5 6 5 10 5 10s3.5-4 3.5-6.5A3.5 3.5 0 0 0 5 0zm0 5a1.5 1.5 0 1 1 0-3 1.5 1.5 0 0 1 0 3z"/></svg>SC Brenval, 1873 Brenval</li>
      <li><svg viewBox="0 0 10 10"><path d="M2 0 3.6 2.4 2.6 3.6a6 6 0 0 0 3.8 3.8l1.2-1L10 8l-1 2C4.5 10 0 5.5 0 1z"/></svg>+41 27 555 01 84</li>
      <li><svg viewBox="0 0 10 10"><path d="M0 2h10v6H0zM.6 2.4 5 5.6l4.4-3.2V3L5 6.2.6 3z"/></svg>first.lastname@scbrenval.ch</li>
      <li><svg viewBox="0 0 10 10"><path d="M5 0a5 5 0 1 0 0 10A5 5 0 0 0 5 0zm0 1c.6 0 1.3 1.4 1.4 3.5H3.6C3.7 2.4 4.4 1 5 1zM1 5.5h1.6c0 1 .2 1.9.5 2.6A4 4 0 0 1 1 5.5zm2.6 0h2.8C6.3 7.6 5.6 9 5 9s-1.3-1.4-1.4-3.5zm3.8 0H9a4 4 0 0 1-2.1 2.6c.3-.7.5-1.6.5-2.6zM1 4.5a4 4 0 0 1 2.1-2.6c-.3.7-.5 1.6-.5 2.6zm6.4 0c0-1-.2-1.9-.5-2.6A4 4 0 0 1 9 4.5z"/></svg>www.scbrenval.ch</li>
    </ul>
  </section>

  <section class="card card--back" aria-label="Verso de la carte">
    <svg class="card-bands" viewBox="0 0 500 324" aria-hidden="true">
      <polygon points="0,0 26,0 26,186 62,222 0,222" fill="var(--club-red)"/>
      <polygon points="84,290 500,290 500,324 118,324" fill="var(--club-blue)"/>
    </svg>
    <div class="club-mark"><span class="club-mark__dot"></span>SC Brenval</div>
  </section>

</main>
</body>
</html>
```